Business Podcaster needs a sexy book cover design for upcoming book launch

I'm launching a book called Chase the Summit: how to accelerate your growth through reaching out, getting a response from, and leaving an impression on the people you admire most. It would be cool to have maybe a band of heroes or a single hero or something on the cover, then I'll need the spine designed, as well as the back cover which would be mostly just quotes about the book from other prominent people.

I dont want to extend it. I want to shorten it. Can I do that?

```html
<!DOCTYPE html>
<html lang="en">
<head>
<meta charset="utf-8">
<title>Chase the Summit – Book Cover Wrap</title>
<link href="https://fonts.googleapis.com/css2?family=Dosis:wght@300;400;500&family=Ubuntu:wght@400&display=swap" rel="stylesheet">
<style>
  :root {
    --page: #ffffff;
    --back-bg: #dcdedf;
    --ink: #262626;
    --body-ink: #2e2e2e;
    --spine-red: #b21f19;
    --title-red: #b8201a;
    --sky-top: #8496a3;
    --sky-mid: #c4c4c0;
    --horizon: #d6a882;
    --ground: #241816;
    --skin-soft: #d9c6b8;
    --white: #ffffff;
  }
  * { margin: 0; padding: 0; box-sizing: border-box; }
  html, body { width: 1200px; height: 1200px; overflow: hidden; background: var(--page); }
  .canvas { position: relative; width: 1200px; height: 1200px; background: var(--page); }
  .wrap { position: absolute; left: 0; top: 152px; width: 1200px; height: 882px; display: flex; }

  /* Back cover */
  .back-cover { position: relative; width: 566px; height: 100%; background: var(--back-bg); overflow: hidden; }
  .back-copy {
    position: absolute; left: 68px; top: 80px; width: 438px;
    font-family: "Dosis", sans-serif; font-weight: 400; font-size: 17.5px;
    line-height: 31.8px; color: var(--body-ink); text-align: justify;
    hyphens: auto; -webkit-hyphens: auto;
  }
  .back-copy .lead { font-size: 32px; font-weight: 400; color: var(--ink); line-height: 1; }
  .back-photo {
    position: absolute; left: 0; top: 530px; width: 566px; height: 352px;
    background: linear-gradient(180deg, var(--back-bg) 0%, var(--skin-soft) 50%, var(--back-bg) 100%);
  }
  .barcode-space { position: absolute; left: 358px; top: 731px; width: 187px; height: 115px; background: var(--white); }

  /* Spine */
  .spine { position: relative; width: 67px; height: 100%; background: var(--spine-red); }
  .spine-title, .spine-author {
    position: absolute; left: 50%; transform-origin: left top;
    white-space: nowrap; font-family: "Dosis", sans-serif;
  }
  .spine-title {
    top: 48px; transform: rotate(90deg) translate(0, -50%);
    font-size: 38px; font-weight: 400; color: var(--ink); letter-spacing: 0.5px;
  }
  .spine-author {
    top: 538px; transform: rotate(90deg) translate(0, -50%);
    font-size: 21px; font-weight: 400; color: var(--white); letter-spacing: 18px;
  }

  /* Front cover */
  .front-cover { position: relative; width: 567px; height: 100%; overflow: hidden; }
  .front-photo {
    position: absolute; inset: 0;
    background: linear-gradient(180deg, var(--sky-top) 0%, var(--sky-mid) 45%, var(--horizon) 72%, #6a3a2a 86%, var(--ground) 100%);
  }
  .front-title {
    position: absolute; left: 0; right: 0; top: 44px; text-align: center;
    font-family: "Dosis", sans-serif; font-weight: 400; line-height: 1;
  }
  .front-title .title-top { display: block; font-size: 92px; color: var(--ink); letter-spacing: 1px; }
  .front-title .title-main { display: block; font-size: 128px; color: var(--title-red); letter-spacing: 4px; margin-top: 6px; }
  .front-subtitle {
    position: absolute; left: 76px; right: 76px; top: 290px; text-align: center;
    font-family: "Ubuntu", sans-serif; font-size: 22px; line-height: 24px; color: var(--ink);
  }
  .front-author {
    position: absolute; left: 0; right: 0; bottom: 24px; text-align: center;
    font-family: "Dosis", sans-serif; font-weight: 500; font-size: 28px;
    letter-spacing: 18px; color: var(--white); padding-left: 18px;
  }
</style>
</head>
<body>
<div class="canvas">
  <div class="wrap">
    <section class="back-cover">
      <div class="back-photo" role="img" aria-label="Photograph of two hands clasped in a handshake"></div>
      <div class="back-copy">
        <p><span class="lead">Lorem ipsum</span> dolor sit amet, consectetur adipiscing elit, sed do eiusmod tempor incididunt ut labore et dolore magna aliqua. Ut enim ad minim veniam, quis nostrud exercitation ullamco laboris nisi ut aliquip ex ea commodo consequat. Duis aute irure dolor in reprehenderit in voluptate velit esse cillum dolore eu fugiat nulla pariatur. Excepteur sint occaecat cupidatat non proident, sunt in culpa qui officia deserunt mollit anim id est laborum.</p>
        <p>Lorem ipsum dolor sit amet, consectetur adipiscing elit, sed do eiusmod tempor incididunt ut labore et dolore magna aliqua. Ut enim ad minim veniam, quis nostrud exercitation ullamco laboris nisi ut aliquip ex ea commodo consequat. Duis aute irure dolor in reprehenderit in voluptate velit esse cillum dolore eu fugiat nulla pariatur.</p>
      </div>
      <div class="barcode-space"></div>
    </section>

    <section class="spine">
      <div class="spine-title">CHASE THE SUMMIT</div>
      <div class="spine-author">AUTHOR NAME</div>
    </section>

    <section class="front-cover">
      <div class="front-photo" role="img" aria-label="Photograph of two caped heroes seen from behind, standing on a hilltop at sunset above a city"></div>
      <h1 class="front-title">
        <span class="title-top">CHASE THE</span>
        <span class="title-main">SUMMIT</span>
      </h1>
      <p class="front-subtitle">How to accelerate your growth through reaching out, getting a response from, and leaving an impression on the people you admire most</p>
      <div class="front-author">AUTHOR NAME</div>
    </section>
  </div>
</div>
</body>
</html>
```